Business Card & Email Signature Design || Upmarket + Luxury

Riverlume Honey, a New Zealand Manuka Honey company needs a Business Card & Email Signature design.

Our logo's are attached in Gold & Black versions, feel free to be creative with how you use the logo and it's patterns in your design.

Style:
- Looking for an Elegant, Luxurious, Upmarket feel.
- Black/Matte Black Card, Gold Foil, UV Embossing

Information to Add:

- Logo
- Company Name: Riverlume Honey
- Name: Mattias Brovell
- Title: Creative Director
- Phone: +64 2919 58 617
- Email: mattias@riverlumehoney.example
- Website: www.riverlumehoney.example

- Socials: ***For email Signature Only***
- Facebook: https://www.facebook.com/riverlumehoney/
- Instagram: https://www.instagram.com/riverlumehoney/

Target Market(s)

Asia/Europe Luxury, Upmarket

Contact Information for Business Card

- Logo
- Name: Mattias Brovell
- Phone: +64 2919 58 617

Font styles to use
Other font styles liked:
• Champagne & Limousines (Attached)

Requirements
Must have
• Business Card & Email Signature Design.

Looking for a Sleek, Luxury, Upmarket Design.

```html
<!DOCTYPE html>
<html lang="en">
<head>
<meta charset="utf-8">
<title>Riverlume Honey – Business Card &amp; Email Signature</title>
<link rel="stylesheet" href="https://fonts.googleapis.com/css2?family=Mulish:wght@400;500;800&display=swap">
<style>
  :root {
    --ink: #333333;
    --ink-soft: #4a4a4a;
    --paper: #ffffff;
    --comb-cream: #ece5c6;
    --comb-light: #f7f3e2;
    --frame: #9a9a9a;
    --shadow: rgba(0, 0, 0, 0.55);
  }
  * { box-sizing: border-box; margin: 0; padding: 0; }
  html, body {
    width: 1200px; height: 1000px; overflow: hidden;
    background: var(--paper);
    font-family: "Mulish", sans-serif;
    color: var(--ink);
  }
  .board { position: relative; width: 1200px; height: 1000px; }

  .card {
    position: absolute; top: 232px; width: 482px; height: 276px;
    background: var(--paper); overflow: hidden;
    box-shadow: 10px 12px 14px var(--shadow);
  }
  .card--front { left: 82px; }
  .card--back { left: 621px; }

  .comb-fill {
    position: absolute;
    background:
      repeating-linear-gradient(90deg, var(--comb-light) 0 18px, var(--comb-cream) 48px, var(--comb-light) 66px);
  }
  .card--front .comb-fill { inset: 0; }
  .card--back .comb-fill {
    top: 0; right: 0; bottom: 0; width: 260px;
    -webkit-mask-image: linear-gradient(90deg, transparent 0%, #000 35%);
    mask-image: linear-gradient(90deg, transparent 0%, #000 35%);
  }

  .brand {
    position: absolute; display: flex; align-items: center; justify-content: center;
    border-radius: 50%; border: 3px solid var(--ink); background: var(--paper);
    text-align: center; font-weight: 500; color: var(--ink);
    letter-spacing: 0.12em; text-transform: uppercase; line-height: 1.35;
  }
  .card--front .brand { left: 128px; top: 25px; width: 226px; height: 226px; font-size: 19px; }
  .card--back .brand { left: 367px; top: 166px; width: 98px; height: 98px; font-size: 9px; border-width: 2px; }

  .person { position: absolute; }
  .person__name { font-weight: 800; letter-spacing: 0.01em; }
  .person__title { font-weight: 400; }

  .card--back .person { left: 22px; top: 62px; }
  .card--back .person__name { font-size: 27px; }
  .card--back .person__title { font-size: 16px; margin-top: 2px; }

  .contact { position: absolute; list-style: none; }
  .contact li { display: flex; align-items: center; gap: 6px; }
  .contact svg { flex: none; }
  .card--back .contact { left: 22px; top: 152px; font-size: 16px; }
  .card--back .contact li + li { margin-top: 4px; }

  .site { position: absolute; font-weight: 500; }
  .card--back .site { left: 23px; top: 234px; font-size: 16px; }

  .signature {
    position: absolute; left: 322px; top: 692px; width: 601px; height: 201px;
    border: 1px solid var(--frame); background: var(--paper); overflow: hidden;
  }
  .signature .comb-fill {
    top: 0; left: 0; bottom: 0; width: 280px;
    -webkit-mask-image: linear-gradient(90deg, #000 60%, transparent 100%);
    mask-image: linear-gradient(90deg, #000 60%, transparent 100%);
  }
  .signature .brand { left: 63px; top: 22px; width: 136px; height: 136px; font-size: 12px; border-width: 2px; }
  .signature .site { left: 0; width: 262px; top: 167px; font-size: 13px; text-align: center; }
  .signature .person { left: 312px; top: 35px; }
  .signature .person__name { font-size: 21px; }
  .signature .person__title { font-size: 14px; }
  .signature .contact { left: 312px; top: 101px; font-size: 14px; }
  .signature .contact li + li { margin-top: 2px; font-size: 13px; }

  .socials { position: absolute; left: 311px; top: 165px; display: flex; gap: 22px; list-style: none; font-size: 13px; }
  .socials li { display: flex; align-items: center; gap: 6px; }
  .socials .dot { width: 15px; height: 15px; border-radius: 50%; background: var(--ink); }
</style>
</head>
<body>
<main class="board">

  <section class="card card--front" aria-label="Business card front">
    <div class="comb-fill" role="img" aria-label="Soft cream honeycomb pattern"></div>
    <div class="brand">Riverlume<br>Honey</div>
  </section>

  <section class="card card--back" aria-label="Business card back">
    <div class="comb-fill" role="img" aria-label="Soft cream honeycomb pattern fading in from the right"></div>
    <div class="person">
      <h1 class="person__name">Mattias Brovell</h1>
      <p class="person__title">Creative Director</p>
    </div>
    <ul class="contact">
      <li>
        <svg width="11" height="17" viewBox="0 0 11 17" aria-hidden="true"><rect x="1" y="1" width="9" height="15" rx="1.5" fill="none" stroke="currentColor" stroke-width="1.6"/><line x1="4" y1="13.2" x2="7" y2="13.2" stroke="currentColor" stroke-width="1.4"/></svg>
        +64 2919 58 617
      </li>
      <li>
        <svg width="13" height="10" viewBox="0 0 13 10" aria-hidden="true"><rect x="0.6" y="0.6" width="11.8" height="8.8" fill="none" stroke="currentColor" stroke-width="1"/><polyline points="0.6,0.8 6.5,5.5 12.4,0.8" fill="none" stroke="currentColor" stroke-width="1"/></svg>
        mattias@riverlumehoney.example
      </li>
    </ul>
    <p class="site">www.riverlumehoney.example</p>
    <div class="brand">Riverlume<br>Honey</div>
  </section>

  <section class="signature" aria-label="Email signature">
    <div class="comb-fill" role="img" aria-label="Soft cream honeycomb pattern fading out to the right"></div>
    <div class="brand">Riverlume<br>Honey</div>
    <p class="site">www.riverlumehoney.example</p>
    <div class="person">
      <h2 class="person__name">Mattias Brovell</h2>
      <p class="person__title">Creative Director</p>
    </div>
    <ul class="contact">
      <li>
        <svg width="9" height="14" viewBox="0 0 11 17" aria-hidden="true"><rect x="1" y="1" width="9" height="15" rx="1.5" fill="none" stroke="currentColor" stroke-width="1.6"/><line x1="4" y1="13.2" x2="7" y2="13.2" stroke="currentColor" stroke-width="1.4"/></svg>
        +64 2919 58 617
      </li>
      <li>
        <svg width="11" height="9" viewBox="0 0 13 10" aria-hidden="true"><rect x="0.6" y="0.6" width="11.8" height="8.8" fill="none" stroke="currentColor" stroke-width="1"/><polyline points="0.6,0.8 6.5,5.5 12.4,0.8" fill="none" stroke="currentColor" stroke-width="1"/></svg>
        mattias@riverlumehoney.example
      </li>
    </ul>
    <ul class="socials">
      <li><span class="dot"></span>riverlumehoney</li>
      <li><span class="dot"></span>riverlumehoney</li>
    </ul>
  </section>

</main>
</body>
</html>
```